We are Coastal Auto Freight Exchange from Japan to NewZealand

we are importing Japanese used cars from Japan to NewZealand and Motor vehicle parts trading in the world. we have company in Japan and New Zealand. we provide one stop service to import car from japan. we have two companies called CAF Ltd for car importing from japan and CAF Lubricants Ltd for car engine oil importing. also we are importing car parts under CAF Autohaus Ltd. we need logo and name card for our company. Company name is CAF LTD (Coastal Auto Freight Exchange) From japan we are sourcing newer European cars and 20-30 years old special sports limited model cars importing specialist. we are not normal car importer and retailer. also we are manufacture and supplying Motor vehicle Engine oil and parts from Korea and japan to New Zealand. Engine oil and part brand name is 'Ultra Zed' we would like to introduce on business card. we want to show what we are doing as car importing, selling, parts and engine oil importing.

Target Market(s)

-Car buyer(customer)
-Mechanic shop
-Car dealers
-Car industry people
-Car & parts exporter/importer
-Engine oil reseller
-parts reseller

Industry/Entity Type

Car Dealer

Contact Information for Business Card

Dana Polk
Director
17 Fernlea Street, Birkdale Heights, Auckland 0754, New Zealand
+64219384051
caf.limited@examplemail.test
www.cafautos.example.nz
www.cafnippon.example.com

Colors
ffc214
9d9d9d
0255a3

Requirements
Must have
• * CAF Autos Ltd(CAF LTD-car importing, sourcing and retailing)
• * CAF Lubricants Ltd(Engine Oil importing, sourcing and retailing)
• * CAF Autohaus Ltd(car parts and accessories importing, sourcing and retailing)
• * Ultra Zed -Brand name of engine oil
• (We are wanting to make logo for CAF AUTOS and ULTRA ZED MOTOR OIL)
Nice to have
• we would like to show us to our clients as professional, trustworthy, many experience. not well known in the market but unique indivisual company for clients.
Should not have
• we do not want to feel just 'car dealer' , 'importer' or normal sales

```html
<!DOCTYPE html>
<html lang="en">
<head>
<meta charset="utf-8">
<title>CAF Autos Ltd – Business Card</title>
<link rel="stylesheet" href="https://fonts.googleapis.com/css2?family=Roboto:wght@300;400;500;700&display=swap">
<style>
  :root {
    --canvas-bg: #e9e7e3;
    --card-blue: #3d3f96;
    --card-yellow: #f7cd4f;
    --text-white: #ffffff;
    --text-grey: #8f8c86;
    --text-grey-dark: #7d7a74;
    --card-shadow: 0 10px 28px rgba(0, 0, 0, 0.18);
  }
  * { box-sizing: border-box; margin: 0; padding: 0; }
  html, body {
    width: 1200px;
    height: 1000px;
    overflow: hidden;
    background: var(--canvas-bg);
    font-family: "Roboto", Arial, sans-serif;
  }
  .canvas {
    position: relative;
    width: 1200px;
    height: 1000px;
  }
  .card {
    position: absolute;
    top: 345px;
    width: 530px;
    height: 310px;
    box-shadow: var(--card-shadow);
  }
  .card--front {
    left: 45px;
    background: var(--card-blue);
    color: var(--text-white);
  }
  .card--back {
    left: 625px;
    background: var(--card-yellow);
    color: var(--text-grey);
  }
  .front__identity {
    position: absolute;
    right: 50px;
    top: 118px;
    display: flex;
    flex-direction: column;
    align-items: flex-end;
    gap: 18px;
  }
  .front__legal-name {
    font-size: 13px;
    font-weight: 300;
    letter-spacing: 0.2px;
    margin-right: 50px;
  }
  .front__brand {
    display: flex;
    align-items: center;
    gap: 12px;
  }
  .brand__name {
    font-size: 30px;
    font-weight: 700;
    letter-spacing: 4px;
    color: var(--text-white);
    white-space: nowrap;
  }
  .brand__dot {
    width: 32px;
    height: 32px;
    border-radius: 50%;
    background: var(--text-white);
  }
  .back__contact {
    position: absolute;
    left: 40px;
    top: 96px;
  }
  .contact__name {
    font-size: 26px;
    font-weight: 300;
    letter-spacing: 0.5px;
    line-height: 30px;
    text-transform: uppercase;
  }
  .contact__role {
    font-size: 26px;
    font-weight: 500;
    line-height: 30px;
    color: var(--text-grey-dark);
    margin-bottom: 18px;
  }
  .contact__line {
    font-size: 15px;
    font-weight: 300;
    line-height: 25px;
    white-space: nowrap;
  }
</style>
</head>
<body>
  <main class="canvas">
    <section class="card card--front" aria-label="Business card front">
      <div class="front__identity">
        <p class="front__legal-name">Coastal Auto Freight Exchange Limited ( RMVT )</p>
        <div class="front__brand">
          <span class="brand__name">CAF AUTOS LTD</span>
          <span class="brand__dot" aria-hidden="true"></span>
        </div>
      </div>
    </section>

    <section class="card card--back" aria-label="Business card back">
      <div class="back__contact">
        <p class="contact__name">Dana Polk</p>
        <p class="contact__role">Director</p>
        <p class="contact__line">caf.limited@examplemail.test</p>
        <p class="contact__line">www.cafautos.example.nz</p>
        <p class="contact__line">www.cafnippon.example.com</p>
        <p class="contact__line">17 Fernlea Street, Birkdale Heights, Auckland 0754, New Zealand</p>
      </div>
    </section>
  </main>
</body>
</html>
```